Web Design Project

We need a web design for a new company that we started called ZARN CNG. ZARN CNG is a company that will build, own and operate compressed natural gas fueling stations throughout the United States. Our primary customers are Trucking companies and the stations will be built for semi trucks. CNG is better for the environment than diesel fuel, and will save trucking companies loads of money. It is also a domestic product which means that it will create American jobs and help America become energy independent. I have attached a logo that we are using. We dont need to stay with this logo persay, but it is what we have for now. We have a video on Vidlo that shows a bit of what we are doing. just search for ZARN CNG. ZARN CNG is a sister company of Holtmark of Arizona,www.hkqvz.example and a nationwide distributor of TRIVEX FUEL, www.trivexfuel.example. We will need links to these sites. Please make any pictures of trucks Holtmark trucks, and please do not use pictures of cabover trucks.

Target Market(s)

The target market are truck drivers and truckers.

Industry/Entity Type

Environment

Requirements
Must have
• Map showing station locations, a page with industry news, a page with a savings calculator (we can code the calculator) Site should have links to

```html
<!DOCTYPE html>
<html lang="en">
<head>
<meta charset="utf-8">
<title>ZARN CNG</title>
<link href="https://fonts.googleapis.com/css2?family=Cinzel:wght@400;700&display=swap" rel="stylesheet">
<style>
:root{
  --teal:#28b9c9;
  --teal-dark:#1497a6;
  --page:#f7f7f7;
  --ink:#111;
  --body:#555;
  --green:#00ff3c;
  --white:#fff;
}
*{margin:0;padding:0;box-sizing:border-box}
html,body{width:1200px;height:1100px;overflow:hidden;background:var(--page)}
body{position:relative;font-family:Arial,Helvetica,sans-serif;color:var(--body)}
.topline{position:absolute;left:0;top:0;width:1200px;height:5px;background:var(--teal-dark)}
.header{position:absolute;left:0;top:5px;width:1200px;height:106px;background:var(--white)}
.band{position:absolute;left:0;top:111px;width:1200px;height:139px;background:var(--teal)}
.brand{position:absolute;left:135px;top:20px;font-family:'Cinzel',serif;color:var(--ink);white-space:nowrap}
.brand .big{font-size:64px;letter-spacing:1px}
.brand .small{font-size:50px;margin-left:10px}
.pump{position:absolute;left:905px;top:18px;width:110px;height:136px;border-radius:6px;background:linear-gradient(180deg,#e9f3ee,#3aa57a 60%,#1b3a2e)}
.nav{position:absolute;left:123px;top:124px;display:flex;font-family:'Cinzel',serif;font-size:19px;color:#1a1a1a;white-space:nowrap}
.nav a{color:inherit;text-decoration:none;margin-right:23px}
.nav a:last-child{margin-right:0}
.hero{position:absolute;left:124px;top:160px;width:932px;height:331px;background:var(--white);box-shadow:0 5px 6px rgba(0,0,0,.35)}
.hero-photo{position:absolute;left:6px;top:4px;width:920px;height:239px;background:linear-gradient(100deg,#3f6d4b 0%,#8e9a92 35%,#d7dde2 55%,#9fb2a9 75%,#c9d2cf 100%)}
.hero-caption{position:absolute;left:6px;top:248px;width:920px;height:56px;background:var(--green);text-align:center;font-family:'Cinzel',serif;color:var(--ink)}
.hero-caption h2{font-weight:400;font-size:22px;margin-top:4px;letter-spacing:.5px}
.hero-caption a{display:inline-block;color:var(--ink);font-size:16px;margin-top:2px}
.hero-strip{position:absolute;left:6px;top:309px;width:920px;height:15px;background:linear-gradient(90deg,#8f9a95,#d9dcd8 60%,#cfc7b5)}
.panel{position:absolute;top:537px;height:290px;background:var(--white);box-shadow:0 0 4px rgba(0,0,0,.15)}
.panel h3{font-family:'Cinzel',serif;font-weight:400;font-size:23px;color:var(--ink);position:absolute;top:12px;white-space:nowrap}
.panel p{position:absolute;line-height:1.2}
.welcome{left:148px;width:377px}
.welcome h3{left:22px}
.welcome p{left:26px;top:56px;width:345px;font-size:14px;line-height:1.22}
.video{left:548px;width:232px}
.video h3{left:11px}
.video .thumb{position:absolute;left:14px;top:63px;width:202px;height:124px;background:linear-gradient(180deg,#2f8a4a 0 4%,#e6e9ec 5% 60%,#d3c7a8 61% 93%,#1c1c1c 94%)}
.video p{left:18px;top:206px;width:205px;font-size:12px}
.news{left:802px;width:232px}
.news h3{left:15px}
.news p{left:16px;top:56px;width:200px;font-size:12px}
.footer{position:absolute;left:0;top:880px;width:1200px;height:220px;background:var(--teal)}
.footer h4{position:absolute;top:24px;font-family:'Cinzel',serif;font-weight:400;font-size:19px;color:var(--ink)}
.connect{left:146px}.find{left:450px}.pages-h{left:808px}
.socials{position:absolute;left:148px;top:74px;display:flex;gap:8px}
.socials span{width:44px;height:44px;border-radius:8px;display:block}
.map{position:absolute;left:449px;top:50px;width:251px;height:84px;background:linear-gradient(120deg,#efe9d8,#cfe1b8 40%,#f2e99a 70%,#e8e4dc)}
.pages{position:absolute;left:810px;top:56px;list-style:none}
.pages li{font-size:13.5px;font-weight:700;color:var(--white);line-height:16.5px;text-shadow:0 1px 1px rgba(0,0,0,.25)}
.rule{position:absolute;left:150px;top:166px;width:900px;height:1px;background:rgba(255,255,255,.35)}
.copy{position:absolute;left:158px;top:186px;font-size:12px;color:var(--white)}
</style>
</head>
<body>
<div class="topline"></div>
<header class="header">
  <div class="brand"><span class="big">ZARN</span><span class="small">CNG</span></div>
  <div class="pump" role="img" aria-label="Illustration of a CNG fuel dispenser"></div>
</header>
<div class="band"></div>
<nav class="nav">
  <a href="#">Home</a>
  <a href="#">About Us</a>
  <a href="#">Services</a>
  <a href="#">Locations</a>
  <a href="#">Savings Calculator</a>
  <a href="#">Contact</a>
</nav>
<section class="hero">
  <div class="hero-photo" role="img" aria-label="Photos of trucks fueling at a CNG station canopy"></div>
  <div class="hero-caption">
    <h2>Lorem ipsum dolor sit amet, consectetur adipisicing elit, sed do eiusmod</h2>
    <a href="#">Read The Full Story</a>
  </div>
  <div class="hero-strip" role="img" aria-label="Edge of next slide photo"></div>
</section>
<section class="panel welcome">
  <h3>Welcome</h3>
  <p>Lorem ipsum dolor sit amet, consectetur adipisicing elit, sed do eiusmod tempor incididunt ut labore et dolore magna aliqua.<br><br>Ut enim ad minim veniam, quis nostrud exercitation ullamco laboris nisi ut aliquip ex ea commodo consequat. Duis aute irure dolor in reprehenderit in voluptate nulla pariatur. Excepteur sint occaecat cupidatat non proident, sunt in culpa qui officia deserunt mollit anim id est laborum.Lorem ipsum dolor sit amet, consectetur adipisicing elit,.</p>
</section>
<section class="panel video">
  <h3>Video Gallery</h3>
  <div class="thumb" role="img" aria-label="Video still of a truck at a CNG station"></div>
  <p>Lorem ipsum dolor sit amet, consectetur adipisicing elit, sed do eiusmod tempor incididunt ut labore et dolore magna aliqua.</p>
</section>
<section class="panel news">
  <h3>Latest News</h3>
  <p>Lorem ipsum dolor sit amet, consectetur adipisicing elit, sed do eiusmod tempor incididunt ut labore et dolore magna aliqua.<br><br>Ut enim ad minim veniam, quis nostrud exercitation ullamco laboris nisi ut aliquip ex ea commodo consequat.<br><br>Duis aute irure dolor in reprehenderit in voluptate nulla pariatur. Excepteur sint occaecat cupidatat non proident.</p>
</section>
<footer class="footer">
  <h4 class="connect">Connect With Us</h4>
  <div class="socials">
    <svg width="44" height="44" viewBox="0 0 44 44" role="img" aria-label="Email"><rect width="44" height="44" rx="8" fill="#7a7a7a"/><rect x="8" y="13" width="28" height="19" rx="2" fill="#f2f2f2"/><path d="M8 14 L22 25 L36 14" fill="none" stroke="#7a7a7a" stroke-width="2"/></svg>
    <svg width="44" height="44" viewBox="0 0 44 44" role="img" aria-label="News feed"><rect width="44" height="44" rx="8" fill="#f39019"/><circle cx="13" cy="31" r="3.5" fill="#fff"/><path d="M10 20a14 14 0 0 1 14 14M10 11a23 23 0 0 1 23 23" fill="none" stroke="#fff" stroke-width="4"/></svg>
    <span role="img" aria-label="Social network link" style="background:#3b5998"></span>
    <span role="img" aria-label="Social network link" style="background:#5fc6ea"></span>
  </div>
  <h4 class="find">Find Us</h4>
  <div class="map" role="img" aria-label="Street map of station location"></div>
  <h4 class="pages-h">Pages</h4>
  <ul class="pages">
    <li>Home</li><li>About Us</li><li>Services</li><li>Locations</li><li>Savings Calculator</li><li>Contact</li>
  </ul>
  <div class="rule"></div>
  <p class="copy">Copyright © 2012 ZARN CNG. Use of this website constitutes acceptance of our User Agreement and Privacy Policy.</p>
</footer>
</body>
</html>
```